Business Card Design - ThriveMetric

Looking for creative, modern design, two sided for ThriveMetric that is consistent with color and feel of website www.thrivemetric.net.

Back of card will be used to promote products or have a quote revolving around decisions, change, leadership, innovation, creativity. Back should also have space to promote website, but optional to use the icon. Front of the card will need to use the icon and have standard place for name, job title, phone and email. We are not looking to put a mailing address or fax. Also want space to place a few words/phrase explaining what we do...such as individual growth and organizational development or tools, training, information...in addition, want the linkpage icon small on the front somewhere as we are also on linkpage.

Vector file uploaded of icon.

Target Market(s)

Professional coaching for individual growth and organizational development

Industry/Entity Type

Business

Requirements
Must have
• Icon...see attached.

```html
<!DOCTYPE html>
<html lang="en">
<head>
<meta charset="utf-8">
<title>ThriveMetric Business Card</title>
<link rel="stylesheet" href="https://fonts.googleapis.com/css2?family=Marcellus&family=Caudex:ital,wght@1,700&display=swap">
<style>
  :root {
    --page: #ececec;
    --sky-light: #a9edfd;
    --sky: #5cc6f1;
    --royal: #3a8cf0;
    --royal-deep: #2d74de;
    --ink: #101418;
    --white: #ffffff;
    --silver: #dfe8ef;
    --icon-blue: #1f6fd8;
  }
  html, body {
    margin: 0;
    padding: 0;
    width: 922px;
    height: 1200px;
    overflow: hidden;
    background: var(--page);
  }
  .canvas {
    position: relative;
    width: 922px;
    height: 1200px;
  }
  .card {
    position: absolute;
    left: 61px;
    width: 800px;
    height: 560px;
    border-radius: 10px;
    overflow: hidden;
    box-shadow: 0 4px 14px rgba(0,0,0,0.18);
  }
  .card-front { top: 30px; background: linear-gradient(160deg, var(--sky) 0%, var(--sky-light) 100%); }
  .card-back { top: 620px; background: var(--sky-light); }
  .card svg { position: absolute; inset: 0; display: block; }
  .body-text { font-family: 'Marcellus', serif; }
  .label-text { font-family: 'Caudex', serif; font-style: italic; font-weight: 700; }
</style>
</head>
<body>
<main class="canvas">

  <!-- Front side -->
  <section class="card card-front">
    <svg width="800" height="560" viewBox="0 0 800 560">
      <defs>
        <radialGradient id="emblemFill" cx="0.4" cy="0.35" r="0.7">
          <stop offset="0" stop-color="#ffffff"/>
          <stop offset="1" stop-color="#b9d3ea"/>
        </radialGradient>
        <linearGradient id="pagesFill" x1="0" y1="0" x2="1" y2="1">
          <stop offset="0" stop-color="#f4f8fb"/>
          <stop offset="1" stop-color="#8fb6d6"/>
        </linearGradient>
      </defs>

      <!-- brand emblem area -->
      <g class="brand-emblem">
        <circle cx="172" cy="175" r="132" fill="url(#emblemFill)" stroke="var(--icon-blue)" stroke-width="6"/>
        <text x="172" y="185" text-anchor="middle" class="body-text" font-size="30" fill="var(--icon-blue)">ThriveMetric</text>
      </g>

      <!-- open book illustration placeholder -->
      <rect class="book-art" role="img" aria-label="Open book illustration" x="0" y="352" width="178" height="66" rx="6" fill="url(#pagesFill)"/>

      <!-- tagline panel -->
      <polygon class="tagline-panel" points="0,398 278,398 470,560 0,560" fill="var(--royal)"/>
      <text class="body-text tagline" font-size="16.5" fill="var(--ink)">
        <tspan x="38" y="452">Providing tools,training,information</tspan>
        <tspan x="38" y="485">and collaboration to achieve the</tspan>
        <tspan x="38" y="518">results you want.</tspan>
      </text>

      <!-- social link pill -->
      <rect class="social-square" x="22" y="530" width="14" height="14" fill="var(--white)"/>
      <rect class="social-pill" x="42" y="528" width="332" height="19" rx="9.5" fill="var(--icon-blue)"/>
      <text class="body-text" x="56" y="542" font-size="13" fill="var(--white)">www.linkpage.com/thrivemetric</text>

      <!-- name bar -->
      <rect class="name-bar" x="419" y="272" width="365" height="46" rx="6" fill="var(--ink)"/>
      <text class="body-text company-name" x="601" y="306" text-anchor="middle" font-size="36" fill="var(--white)">ThriveMetric</text>

      <!-- personal details -->
      <text class="label-text" x="472" y="352" font-size="24" fill="var(--ink)">Name-</text>
      <text class="label-text" x="472" y="382" font-size="24" fill="var(--ink)">Job Title-</text>

      <!-- contact icons -->
      <g class="contact-icons">
        <circle cx="491" cy="423" r="21" fill="#8fd4f5" stroke="var(--icon-blue)" stroke-width="3"/>
        <path d="M480 425 L491 414 L502 425 M483 423 V433 H499 V423" fill="none" stroke="var(--white)" stroke-width="3" stroke-linejoin="round"/>

        <circle cx="491" cy="477" r="21" fill="var(--icon-blue)" stroke="#9ad7f4" stroke-width="3"/>
        <path d="M483 467 q-2 4 2 11 q5 7 11 9 l4 -4 l-5 -4 l-3 2 q-4 -2 -6 -7 l2 -3 l-3 -5 z" fill="var(--white)"/>

        <circle cx="491" cy="526" r="21" fill="#6fa8dc" stroke="var(--icon-blue)" stroke-width="3"/>
        <circle cx="491" cy="526" r="7" fill="none" stroke="var(--white)" stroke-width="4" stroke-dasharray="3 2"/>
      </g>
    </svg>
  </section>

  <!-- Back side -->
  <section class="card card-back">
    <svg width="800" height="560" viewBox="0 0 800 560">
      <defs>
        <linearGradient id="bandFill" x1="0" y1="0" x2="0" y2="1">
          <stop offset="0" stop-color="var(--royal-deep)"/>
          <stop offset="1" stop-color="var(--royal)"/>
        </linearGradient>
        <symbol id="pointer" viewBox="0 0 16 12">
          <path d="M0 3 H9 V0 L16 6 L9 12 V9 H0 Z" fill="var(--ink)"/>
        </symbol>
      </defs>

      <g transform="translate(400 290) rotate(-22)">
        <rect class="quote-band" x="-700" y="-175" width="1400" height="340" fill="url(#bandFill)"/>
        <line x1="-700" y1="-175" x2="700" y2="-175" stroke="var(--ink)" stroke-width="3"/>

        <text class="label-text heading" x="-345" y="-190" font-size="34" fill="var(--ink)">THRIVEMETRIC</text>

        <g class="quotes body-text" font-size="15.5" fill="var(--ink)">
          <use href="#pointer" x="-355" y="-158" width="16" height="12"/>
          <text x="-334" y="-147">"Life is not fair - get used to it."</text>
          <use href="#pointer" x="-355" y="-136" width="16" height="12"/>
          <text x="-334" y="-125">"Try not to become a man of success, but rather a man of value."</text>
          <use href="#pointer" x="-355" y="-114" width="16" height="12"/>
          <text x="-334" y="-103">"We are what we repeatedly do. Excellence is not an act, it is a habit."</text>
          <use href="#pointer" x="-355" y="-92" width="16" height="12"/>
          <text x="-334" y="-81">"The measure of a man is the way he bears up under misfortune."</text>
          <use href="#pointer" x="-355" y="-70" width="16" height="12"/>
          <text x="-334" y="-59">"My decision to start a new one is just that, a decision, since I never get inspirations."</text>
          <use href="#pointer" x="-355" y="-48" width="16" height="12"/>
          <text x="-334" y="-37">"You learn when you listen. You earn when you listen—not just money, but respect."</text>
          <use href="#pointer" x="-355" y="-26" width="16" height="12"/>
          <text x="-334" y="-15">"Leadership is a matter of having people look at you and gain confidence, seeing</text>
          <text x="-310" y="7">how you react. If you're in control, they're in control."</text>
          <use href="#pointer" x="-355" y="18" width="16" height="12"/>
          <text x="-334" y="29">"You don't have to reinvent the wheel, just attach it to a new wagon."</text>
          <use href="#pointer" x="-355" y="40" width="16" height="12"/>
          <text x="-334" y="51">"Every man I meet is my superior in some way."</text>
          <use href="#pointer" x="-355" y="62" width="16" height="12"/>
          <text x="-334" y="73">"Simplicity is the ultimate sophistication."</text>
        </g>

        <rect class="web-bar" x="-60" y="110" width="560" height="44" rx="14" fill="var(--ink)"/>
        <text class="label-text" x="0" y="141" font-size="28" fill="var(--white)">www.thrivemetric.net</text>
      </g>

      <!-- corner brand mark -->
      <g class="corner-brand">
        <circle cx="654" cy="490" r="10" fill="var(--ink)"/>
        <text class="body-text" x="670" y="496" font-size="16" fill="var(--ink)">ThriveMetric</text>
      </g>
    </svg>
  </section>

</main>
</body>
</html>
```